kn stationary
knbizcards
Simple
Harold T. Pemberly, PhD
CEO
218 Copperfield Lane, Suite 300 Jackson, MS 39211
htp@kestonnetworksllc.com
www.kestonnetworksllc.com

```html
<!DOCTYPE html>
<html lang="en">
<head>
<meta charset="utf-8">
<title>Harold T. Pemberly, PhD – Business Card</title>
<link rel="stylesheet" href="https://fonts.googleapis.com/css2?family=Montserrat:wght@400;500;700;800&display=swap">
<style>
  :root {
    --card-white: #ffffff;
    --ink: #1b1b1b;
    --brand-red: #b8121c;
    --muted: #4a4a4a;
  }
  * { box-sizing: border-box; margin: 0; padding: 0; }
  html, body {
    width: 1200px;
    height: 751px;
    overflow: hidden;
    background: var(--card-white);
  }
  .business-card {
    position: relative;
    width: 1200px;
    height: 751px;
    background: var(--card-white);
    font-family: "Montserrat", sans-serif;
    color: var(--ink);
    text-align: center;
  }
  .brand {
    position: absolute;
    top: 145px;
    left: 0;
    width: 100%;
    display: flex;
    justify-content: center;
    align-items: center;
    gap: 30px;
  }
  .brand-dot {
    width: 70px;
    height: 70px;
    border-radius: 50%;
    background: var(--brand-red);
  }
  .brand-name {
    font-weight: 800;
    font-size: 74px;
    letter-spacing: 2px;
    color: var(--ink);
    line-height: 1;
  }
  .person-name {
    position: absolute;
    top: 385px;
    width: 100%;
    font-weight: 700;
    font-size: 40px;
    color: var(--brand-red);
  }
  .person-title {
    position: absolute;
    top: 435px;
    width: 100%;
    font-weight: 400;
    font-size: 30px;
    color: var(--muted);
  }
  .contact {
    position: absolute;
    top: 530px;
    width: 100%;
    font-size: 32px;
    font-weight: 500;
    line-height: 52px;
    color: var(--ink);
  }
  .contact-label {
    color: var(--brand-red);
    font-weight: 800;
  }
</style>
</head>
<body>
  <main class="business-card">
    <div class="brand">
      <span class="brand-dot" aria-hidden="true"></span>
      <span class="brand-name">KESTON NETWORKS LLC</span>
    </div>

    <p class="person-name">Harold T. Pemberly, PhD</p>
    <p class="person-title">CEO</p>

    <div class="contact">
      <p class="contact-address">218 Copperfield Lane, Suite 300 Jackson, MS 39211</p>
      <p><span class="contact-label">P</span> : 601-555-0142 <span class="contact-label">C</span> : 601-555-0187</p>
      <p><span class="contact-label">F</span> : 601-555-0163 <span class="contact-label">E</span> : htp@kestonnetworksllc.com</p>
      <p><span class="contact-label">W</span> : www.kestonnetworksllc.com</p>
    </div>
  </main>
</body>
</html>
```